Commercial Cleaning Company Needs A Flyer

We are a commercial cleaning company based in London.
We are currently trying to grow our client base and would like a fresh, professional flyer that differentiates us from the competition. We mainly specialises in commercial cleaning such as offices, educational facilities etc. I would like to see a flyer design that look professional, unique not cheap. I have attached a file that contains some company details but Im happy to explore other options if thay are relevant. Please also find company logo and colour chart, this should remain as is.

I have attached some pictures that contain diamond shaped windows. I feel that this can be used to represent and incorporate the logo. Please add to flyer where possible.

Please feel free to contact me for any further advice.
Thanks and good luck

Target Market(s)

commercial buildings and residential property owners

Industry/Entity Type

Cleaning Service

Contact Information for Business Card

Please refer to up loaded document for company details and logo colours.

Font styles to use
Sans Serif

Colors
33a6d7
33b8a4

Requirements
Must have
• Look Professional, not cheap, unique, stand out from others.

```html
<!DOCTYPE html>
<html lang="en">
<head>
<meta charset="utf-8">
<title>Brightline Office Care – Flyer</title>
<link rel="stylesheet" href="https://fonts.googleapis.com/css2?family=Oswald:wght@300;400;500&family=Roboto+Condensed:wght@400&family=Montserrat:wght@400&display=swap">
<style>
  :root {
    --brand-blue: #3cb4e4;
    --brand-green: #3fd9a4;
    --panel-blue: #46d0fb;
    --deep-navy: #0c3c50;
    --band-navy: #1c5068;
    --accent-blue: #2a8fd0;
    --paper: #f3fbfd;
    --ink: #2b4a55;
    --ink-dark: #0e1f26;
    --white: #ffffff;
  }
  * { margin: 0; padding: 0; box-sizing: border-box; }
  html, body { width: 883px; height: 1200px; overflow: hidden; background: var(--paper); }
  .flyer { position: relative; width: 883px; height: 1200px; overflow: hidden; background: var(--paper); }
  .shapes { position: absolute; inset: 0; }

  .brand-name {
    position: absolute; left: 34px; top: 170px; width: 380px; text-align: center;
    font-family: 'Oswald', sans-serif; font-weight: 500; font-size: 36px;
    color: var(--brand-blue); letter-spacing: 0.5px; line-height: 1;
  }
  .tagline {
    position: absolute; left: 34px; top: 214px; width: 380px; text-align: center;
    font-family: 'Roboto Condensed', sans-serif; font-size: 22px; color: var(--brand-green); line-height: 1;
  }
  .headline { position: absolute; left: 35px; top: 268px; font-family: 'Oswald', sans-serif; font-weight: 300; line-height: 1; }
  .headline span { display: block; }
  .headline .line-1 { font-size: 36px; color: var(--brand-green); }
  .headline .line-2 { font-size: 39px; color: var(--brand-blue); font-weight: 400; margin-top: 6px; }
  .headline .line-3 { font-size: 33px; color: var(--brand-green); margin-top: 8px; }

  .about { position: absolute; left: 35px; top: 414px; width: 323px; }
  .about h2 {
    font-family: 'Oswald', sans-serif; font-weight: 400; font-size: 21px; color: var(--brand-blue);
    text-decoration: underline; text-underline-offset: 4px; margin-bottom: 14px;
  }
  .about p {
    font-family: 'Montserrat', sans-serif; font-size: 13.6px; line-height: 23px;
    color: var(--ink); text-align: justify; margin-bottom: 6px;
  }

  .contact { position: absolute; left: 35px; top: 1004px; font-family: 'Roboto Condensed', sans-serif; color: var(--white); }
  .contact h3 { font-family: 'Oswald', sans-serif; font-weight: 400; font-size: 19px; margin-bottom: 12px; }
  .contact h3 em { font-style: normal; color: var(--brand-blue); }
  .contact ul { list-style: none; }
  .contact li { display: flex; align-items: center; height: 34px; font-size: 21px; }
  .contact svg { width: 20px; height: 16px; margin-right: 16px; fill: var(--brand-blue); stroke: var(--brand-blue); }

  .features { position: absolute; left: 470px; top: 560px; width: 370px; text-align: center; font-family: 'Montserrat', sans-serif; color: var(--ink-dark); }
  .feature { position: absolute; left: 0; width: 370px; }
  .feature svg { display: block; margin: 0 auto 8px; width: 48px; height: 48px; fill: none; stroke: var(--white); stroke-width: 3; stroke-linecap: round; stroke-linejoin: round; }
  .feature h4 { font-family: 'Oswald', sans-serif; font-weight: 400; font-size: 20px; color: var(--white); margin-bottom: 8px; }
  .feature p { font-size: 16.5px; line-height: 22px; }
  .feature p.small { font-size: 14.5px; line-height: 17px; }
</style>
</head>
<body>
<div class="flyer">
  <svg class="shapes" width="883" height="1200" viewBox="0 0 883 1200">
    <polygon points="296,0 441,0 441,183" fill="#3fd9a4"/>
    <polygon points="330,0 441,0 441,115" fill="#1f9e78"/>
    <rect x="441" y="0" width="442" height="1200" fill="#ffffff"/>
    <polygon points="441,0 865,0 865,336 441,506" fill="#5a7a7c" role="img" aria-label="City skyline viewed through the diamond-shaped steel lattice windows of a tower"/>
    <polygon points="441,506 506,482 506,560" fill="#1c6aa8"/>
    <polygon points="441,587 861,430 861,1200 441,1200" fill="var(--panel-blue)"/>
    <polygon points="861,662 883,652 883,1200 861,1200" fill="var(--deep-navy)"/>
    <polygon points="0,989 441,823 441,1200 0,1200" fill="var(--band-navy)" role="img" aria-label="Bright modern office interior"/>
    <polygon points="0,989 441,823 441,830 0,996" fill="#46c8f0"/>
    <polygon points="0,876 161,924 0,989" fill="var(--accent-blue)"/>
  </svg>

  <div class="brand-name">BRIGHTLINE OFFICE CARE</div>
  <div class="tagline">Helping your business shine</div>

  <h1 class="headline">
    <span class="line-1">WE'RE MAKING</span>
    <span class="line-2">LONDON BRIGHTER</span>
    <span class="line-3">ONE OFFICE AT A TIME!</span>
  </h1>

  <section class="about">
    <h2>ABOUT US</h2>
    <p>Brightline Office Care continual commitment and dedication to delivering a quality service has enabled us to build a solid foundation within the cleaning industry.</p>
    <p>Our principle and objectives are simple, provide our customers with an affordable quality service to suit their needs and always put our clients first.</p>
    <p>BOC rewards dependability, integrality and providethe training and development for all employees to achieve the best possible results. We believe that building relationships based on ethical conduct towards employees and clientele defines our unique working environments and is a vital key to our success.</p>
  </section>

  <section class="contact">
    <h3><em>FOR MORE</em> INFORMATION :</h3>
    <ul>
      <li><svg viewBox="0 0 20 16"><rect x="1" y="2" width="18" height="12" fill="none" stroke-width="2"/><path d="M1 2 L10 9 L19 2" fill="none" stroke-width="2"/></svg>hello@brightlineofficecare.com</li>
      <li><svg viewBox="0 0 20 16"><rect x="3" y="2" width="14" height="9" fill="none" stroke-width="2"/><rect x="0" y="13" width="20" height="2" stroke="none"/></svg>brightlineofficecare.com</li>
      <li><svg viewBox="0 0 20 16" stroke="none"><path d="M4 1 L8 5 L6 7 Q8 11 12 12 L14 10 L18 13 L15 16 Q3 14 1 4 Z"/></svg>07700900418</li>
      <li><svg viewBox="0 0 20 16" stroke="none"><path d="M1 5 Q10 -1 19 5 L17 8 L14 6 L14 4 Q10 3 6 4 L6 6 L3 8 Z"/><rect x="4" y="9" width="12" height="7" rx="1"/></svg>02079460735</li>
    </ul>
  </section>

  <div class="features">
    <div class="feature" style="top:0">
      <svg viewBox="0 0 48 48"><path d="M18 30 Q12 25 13 19 A11 11 0 0 1 35 19 Q36 25 30 30 L30 36 L18 36 Z"/><path d="M20 40 H28"/><path d="M24 2 V5 M8 8 L10 10 M40 8 L38 10 M3 20 H6 M42 20 H45"/></svg>
      <h4>SPARKLING SERVICE</h4>
      <p>We deliver a sparkling service from<br>start to finish.</p>
    </div>
    <div class="feature" style="top:152px">
      <svg viewBox="0 0 48 48"><path d="M14 44 V34 Q6 28 8 17 Q11 4 25 4 Q38 5 39 18 L43 26 L38 27 V35 H31 V44"/><circle cx="24" cy="19" r="5"/><path d="M27 23 L32 28"/></svg>
      <h4>HUMAN SUPPORT</h4>
      <p>Real support from people who<br>know the business.</p>
    </div>
    <div class="feature" style="top:302px">
      <svg viewBox="0 0 48 48"><circle cx="24" cy="20" r="14"/><circle cx="24" cy="20" r="9"/><path d="M16 32 L12 44 L18 41 L21 46 L24 35 M32 32 L36 44 L30 41 L27 46 L24 35"/></svg>
      <h4>QUALITY CLEANERS</h4>
      <p class="small">Our staff have been trained to uphold<br>our values of attention to detail,<br>perfection and service.</p>
    </div>
    <div class="feature" style="top:460px">
      <svg viewBox="0 0 48 48"><path d="M14 18 L30 38 Q35 43 40 38 Q44 33 39 28 L22 8 Q18 4 14 8 Q11 12 14 16 L28 33"/></svg>
      <h4>COMPETITIVE PRICING</h4>
      <p class="small">Value for money so your office and your<br>bank account sparkles.</p>
    </div>
  </div>
</div>
</body>
</html>
```